Corvane Solutions GAP Brochure Design Project

We are looking for a designer to create a point of sale brochure, the item will be used by Motor Dealers when they are selling our product to their customers, the product is an insurance product that covers the difference between the purchase price of the vehicle and the amount offered by the insurance company in the event the car is stolen or written off by the insurance company. Therefore we are look at a Business to Retail Customer relationship.
Please note we are in the process of designing a logo via Plimbrook that will need to be used in the brochure. I have attached an example of a competitors POS. I am not concerned about including all of the terms and conditions and would prefer to keep the design as a two sided folded but obviously we will need some space for text. This is used by sales people as a sales aid.
Reason: The reference document did not upload, please let me know if you need further information.

```html
<!DOCTYPE html>
<html lang="en">
<head>
<meta charset="utf-8">
<title>Corvane Solutions – Brochure Outside</title>
<link href="https://fonts.googleapis.com/css2?family=Asap+Condensed:wght@400;600;700&family=PT+Sans:wght@400&display=swap" rel="stylesheet">
<style>
  :root {
    --page-bg: #f2f2f2;
    --paper: #ffffff;
    --ink-grey: #58595b;
    --band-grey: #7a7c7f;
    --brand-red: #d71f26;
    --deep-red: #9e1419;
    --bright-red: #ed1c24;
    --white: #ffffff;
  }
  * { margin: 0; padding: 0; box-sizing: border-box; }
  html, body { width: 1200px; height: 767px; overflow: hidden; background: var(--page-bg); }
  .brochure {
    position: absolute; left: 119px; top: 4px;
    width: 962px; height: 758px;
    background: var(--paper);
    overflow: hidden;
    font-family: "Asap Condensed", "Arial Narrow", sans-serif;
  }
  .cover-top { position: absolute; left: 0; top: 0; width: 100%; height: 349px; background: var(--paper); }
  .divider-band { position: absolute; left: 0; top: 349px; width: 100%; height: 18px; background: var(--band-grey); }
  .cover-bottom {
    position: absolute; left: 0; top: 371px; width: 100%; height: 387px;
    background: radial-gradient(ellipse 420px 260px at 140px 150px, var(--bright-red) 0%, var(--brand-red) 40%, var(--deep-red) 100%);
    overflow: hidden;
  }
  .wave { position: absolute; left: 0; top: 0; width: 100%; height: 100%; }
  .tagline { position: absolute; left: 106px; top: 172px; color: var(--ink-grey); }
  .tagline-lead { display: block; font-size: 36px; font-weight: 400; letter-spacing: -0.5px; line-height: 1; padding-left: 38px; }
  .tagline-lead .accent { color: var(--brand-red); }
  .tagline-main { display: block; font-size: 56px; font-weight: 700; letter-spacing: -2px; line-height: 1; margin-top: 2px; }
  .tagline-main .accent { color: var(--brand-red); }
  .brand-name { font-weight: 600; letter-spacing: -1px; line-height: 1; white-space: nowrap; }
  .brand-top { position: absolute; left: 630px; top: 93px; font-size: 42px; color: var(--ink-grey); }
  .brand-bottom { position: absolute; left: 104px; top: 589px; font-size: 42px; color: var(--white); }
  .contact {
    position: absolute; left: 108px; top: 633px;
    font-family: "PT Sans", Arial, sans-serif; font-size: 14px; line-height: 18px; color: var(--white);
  }
  .vehicle-photo {
    position: absolute; left: 505px; top: 382px; width: 470px; height: 360px;
    border-radius: 180px 0 0 180px;
    background: linear-gradient(160deg, #d9d9da 0%, #a9aaab 45%, #6e6e70 75%, #e8ddd0 100%);
  }
</style>
</head>
<body>
  <main class="brochure">
    <section class="cover-top">
      <p class="tagline">
        <span class="tagline-lead"><span class="accent">...your</span> choice</span>
        <span class="tagline-main">for succe<span class="accent">ss</span></span>
      </p>
      <p class="brand-name brand-top">Corvane Solutions</p>
    </section>
    <div class="divider-band"></div>
    <section class="cover-bottom">
      <svg class="wave" viewBox="0 0 962 387" preserveAspectRatio="none" aria-hidden="true">
        <path d="M0 170 C200 120 420 250 962 200 L962 387 L0 387 Z" fill="#ffffff" opacity="0.06"/>
        <path d="M0 260 C250 200 500 330 962 280 L962 387 L0 387 Z" fill="#ffffff" opacity="0.07"/>
        <path d="M0 320 C260 280 520 370 962 340 L962 387 L0 387 Z" fill="#7a0d11" opacity="0.25"/>
      </svg>
    </section>
    <div class="vehicle-photo" role="img" aria-label="Photo of a silver sedan seen from the rear quarter in a softly lit showroom"></div>
    <p class="brand-name brand-bottom">Corvane Solutions</p>
    <address class="contact">
      CONTACT A REPRESENTATIVE TODAY:<br>
      18 Harrow Lane Eastbrook,<br>
      State 60214 USA<br>
      (555) 210-4471&nbsp; (800) 555-0192<br>
      (555) 210-4472 fax<br>
      www.corvanesolutions.com
    </address>
  </main>
</body>
</html>
```